Business Card Design Project

We need a business card for our new business based in Vancouver called
"Sollu⁵ Calm Spa" We are looking for a simple yet bold design for our business cards that will enable us to stand out from the pack. All business card details will be provided in the handover stage.
Updates

Thank you to all who have submitted

The work is great for the most part
Cards with creative use of the logo
have been more successful so far

Dark cards and rounded edges 
are also getting good reviews

Double sided is an option we would like to see explored

Thank you

Target Market(s)

Our clients are stressed business people, yoga/meditation enthusiast, and people looking for a new experience in a Spa enviroment

Industry/Entity Type

Business

Font styles to use
Other font styles liked:
• please check design file

Requirements
Must have
• Sollu⁵ Calm Spa

2417 E Fenwick Row, Vancouver, BC V5K 3H9

sollu@calmspa-example.ca
Nice to have
• Creative approach to layout and design

Outside of the box design elements
Should not have
• Should not be too busy

```html
<!DOCTYPE html>
<html lang="en">
<head>
<meta charset="utf-8">
<title>Sollu 5 Calm Spa – Business Card</title>
<link rel="stylesheet" href="https://fonts.googleapis.com/css2?family=Nunito+Sans:wght@400&display=swap">
<style>
  :root {
    --page-bg: #d9d9db;
    --card-bg: #ffffff;
    --band-bg: #f7f7f9;
    --brand-navy: #2e2f8c;
    --text-grey: #8a8a8e;
  }
  * { margin: 0; padding: 0; box-sizing: border-box; }
  html, body {
    width: 1200px;
    height: 900px;
    overflow: hidden;
    background: var(--page-bg);
  }
  .stage {
    width: 1200px;
    height: 900px;
    display: flex;
    align-items: center;
    justify-content: center;
  }
  .business-card {
    position: relative;
    width: 840px;
    height: 480px;
    background: var(--card-bg);
    overflow: hidden;
    box-shadow: 0 12px 30px rgba(0, 0, 0, 0.18);
  }
  .light-band {
    position: absolute;
    left: 0;
    right: 0;
    top: 78px;
    height: 250px;
    background: var(--band-bg);
  }
  .card-content {
    position: absolute;
    left: 0;
    right: 0;
    top: 104px;
    display: flex;
    flex-direction: column;
    align-items: center;
    font-family: "Nunito Sans", sans-serif;
    font-weight: 400;
  }
  .brand {
    display: flex;
    align-items: center;
    gap: 22px;
    margin-bottom: 44px;
  }
  .brand-dot {
    width: 64px;
    height: 64px;
    border-radius: 50%;
    background: var(--brand-navy);
  }
  .brand-name {
    font-size: 52px;
    letter-spacing: 1px;
    color: var(--brand-navy);
    white-space: nowrap;
  }
  .address,
  .email {
    color: var(--text-grey);
    white-space: nowrap;
  }
  .address { font-size: 24px; margin-bottom: 18px; }
  .email { font-size: 22px; }
</style>
</head>
<body>
  <main class="stage">
    <section class="business-card">
      <div class="light-band"></div>
      <div class="card-content">
        <div class="brand">
          <span class="brand-dot"></span>
          <span class="brand-name">Sollu 5 Calm Spa</span>
        </div>
        <p class="address">2417 E Fenwick Row, Vancouver, BC V5K 3H9</p>
        <p class="email">sollu@calmspa-example.ca</p>
      </div>
    </section>
  </main>
</body>
</html>
```